BrivaTrek Freight Services Business cards

Would like a very unique design catchy but professional for business cards. Please use log provided.Marlon WellsCeo and Founder TransCon Logistix Solutions1-888-913-3225mwells@tlsolutionsus.comwww.bfservicesco.com

```html
<!DOCTYPE html>
<html lang="en">
<head>
<meta charset="utf-8">
<title>BrivaTrek Freight Services – Business Cards</title>
<link rel="stylesheet" href="https://fonts.googleapis.com/css2?family=Roboto:wght@400;500;700&display=swap">
<style>
  :root {
    --backdrop: #262626;
    --card-white: #ffffff;
    --brand-blue: #1473bf;
    --brand-red: #e81c2a;
    --text-grey: #4a4a4a;
    --rule-grey: #b5b5b5;
  }
  * { margin: 0; padding: 0; box-sizing: border-box; }
  html, body {
    width: 1125px;
    height: 1200px;
    overflow: hidden;
    background: var(--backdrop);
    font-family: "Roboto", Arial, sans-serif;
  }
  .canvas { position: relative; width: 1125px; height: 1200px; }

  .card {
    position: absolute;
    left: 171px;
    width: 800px;
    height: 457px;
    overflow: hidden;
  }
  .card--front { top: 106px; background: var(--card-white); }
  .card--back { top: 639px; background: var(--brand-blue); }

  /* Front */
  .brand-lockup {
    position: absolute;
    left: 60px;
    top: 175px;
    width: 360px;
    display: flex;
    align-items: center;
    gap: 14px;
  }
  .brand-lockup__square {
    flex: 0 0 auto;
    width: 40px;
    height: 40px;
    background: var(--brand-red);
  }
  .brand-lockup__name {
    font-weight: 700;
    font-size: 27px;
    line-height: 1.15;
    color: var(--brand-blue);
  }
  .divider {
    position: absolute;
    left: 425px;
    top: 137px;
    width: 2px;
    height: 183px;
    background: var(--rule-grey);
  }
  .contact {
    position: absolute;
    left: 447px;
    top: 130px;
    color: var(--text-grey);
  }
  .contact__name {
    font-size: 31px;
    font-weight: 700;
    color: var(--brand-blue);
    line-height: 1.1;
  }
  .contact__title {
    font-size: 20px;
    font-weight: 500;
    color: var(--brand-red);
    margin-top: 2px;
  }
  .contact__company {
    font-size: 19px;
    margin-top: 24px;
  }
  .contact__list { list-style: none; margin-top: 8px; }
  .contact__item {
    display: flex;
    align-items: center;
    gap: 11px;
    font-size: 19px;
    line-height: 25.5px;
  }
  .contact__icon { width: 18px; height: 18px; flex: 0 0 auto; }
  .stripe-red {
    position: absolute; left: 0; right: 0; top: 440px; height: 4px;
    background: var(--brand-red);
  }
  .stripe-blue {
    position: absolute; left: 0; right: 0; top: 446px; height: 11px;
    background: var(--brand-blue);
  }

  /* Back */
  .back-lockup {
    position: absolute;
    left: 0; right: 0;
    top: 150px;
    display: flex;
    justify-content: center;
    align-items: center;
    gap: 26px;
  }
  .back-lockup__square {
    width: 90px; height: 90px;
    background: var(--brand-red);
  }
  .back-lockup__name {
    font-weight: 700;
    font-size: 52px;
    line-height: 1.1;
    color: var(--card-white);
  }
  .back-web {
    position: absolute;
    left: 0; right: 0;
    top: 398px;
    text-align: center;
    color: var(--card-white);
    font-size: 19px;
    letter-spacing: 6px;
  }
</style>
</head>
<body>
<div class="canvas">

  <section class="card card--front">
    <div class="brand-lockup">
      <span class="brand-lockup__square"></span>
      <span class="brand-lockup__name">BrivaTrek Freight Services</span>
    </div>
    <div class="divider"></div>
    <div class="contact">
      <div class="contact__name">DUSTIN HARROW</div>
      <div class="contact__title">CEO &amp; FOUNDER</div>
      <div class="contact__company">BrivaTrek Freight Services</div>
      <ul class="contact__list">
        <li class="contact__item">
          <svg class="contact__icon" viewBox="0 0 24 24"><path fill="#1473bf" d="M6.6 10.8c1.4 2.8 3.8 5.1 6.6 6.6l2.2-2.2c.3-.3.7-.4 1-.2 1.1.4 2.3.6 3.6.6.6 0 1 .4 1 1V20c0 .6-.4 1-1 1C10.6 21 3 13.4 3 4c0-.6.4-1 1-1h3.5c.6 0 1 .4 1 1 0 1.3.2 2.5.6 3.6.1.3 0 .7-.2 1z"/></svg>
          1-888-472-6081
        </li>
        <li class="contact__item">
          <svg class="contact__icon" viewBox="0 0 24 24"><rect x="2" y="5" width="20" height="14" fill="#1473bf"/><path d="M2 5l10 8 10-8" fill="none" stroke="#fff" stroke-width="1.8"/></svg>
          dharrow@bfservicesco.com
        </li>
        <li class="contact__item">
          <svg class="contact__icon" viewBox="0 0 24 24"><circle cx="12" cy="12" r="10" fill="#1473bf"/><path d="M7 7c2 0 3 1 3 3s-2 2-2 4 1 3 1 5M14 4c0 2 1 3 3 3s3 2 3 3M15 13c1 0 2 1 2 2s-1 3-2 4" fill="none" stroke="#fff" stroke-width="1.6"/></svg>
          www.bfservicesco.com
        </li>
      </ul>
    </div>
    <div class="stripe-red"></div>
    <div class="stripe-blue"></div>
  </section>

  <section class="card card--back">
    <div class="back-lockup">
      <span class="back-lockup__square"></span>
      <span class="back-lockup__name">BrivaTrek<br>Freight Services</span>
    </div>
    <div class="back-web">www.bfservicesco.com</div>
  </section>

</div>
</body>
</html>
```